Update Old OR create new Website

Current Website is looking a bit old, I did this one a few years back.

Would like a fresh new look, current website sitepress theme is " the Vanta theme" from plumcrate and I just purchased this theme - "bravlo" also from plumcrate, I quite like the look of - http://bravlo.quorvex-skins.com/tech-business/ and if we could get somthing simlar would be great.

current website is at http://www.hle.com.au, have been playing around with the slider that i like.

I have said 5 pages to be designed but really it is just a 5 page website where most pages will look the same.

Any questions please let me know

Target Market(s)

Business

Coding

Coded - Design and coding required

Number of Pages Required

5+ page

Font styles to use
Sans Serif

Colors
33a6d7
0292cd
ffffff
0255a3

Requirements
Must have
• Device compatibility - pc, tablet, phone
Nice to have
• video
Should not have
• vunerabilities. Must also use images that will expire or disappear, ie must be uploaded to site not links to elsewhere.

```html
<!DOCTYPE html>
<html lang="en">
<head>
<meta charset="utf-8">
<title>Halvex Technologies</title>
<link rel="stylesheet" href="https://fonts.googleapis.com/css2?family=Raleway:wght@400;500;600;700;800&family=Open+Sans:wght@400;600&display=swap">
<style>
:root{
  --sky:#33a6d7;
  --cyan:#0292cd;
  --navy:#0255a3;
  --white:#ffffff;
  --ink:#2b2f36;
  --muted:#7d838c;
  --soft:#f4f5f7;
  --line:#e3e6ea;
  --dark:#1f2227;
  --darker:#17191d;
  --green:#9ccc3c;
}
*{margin:0;padding:0;box-sizing:border-box}
html,body{width:1200px;height:2588px;overflow:hidden;background:var(--white)}
body{font-family:"Open Sans",Arial,sans-serif;color:var(--ink);font-size:13px;line-height:1.6}
h1,h2,h3,h4,.nav,.btn{font-family:"Raleway",Arial,sans-serif}
.wrap{width:1040px;margin:0 auto;position:relative}

.topbar{height:28px;background:var(--white);border-bottom:1px solid var(--line);font-size:11px;color:var(--muted)}
.topbar .wrap{display:flex;justify-content:space-between;align-items:center;height:28px}
.topbar span{margin-right:20px}

.header{height:72px;background:var(--white);box-shadow:0 1px 4px rgba(0,0,0,.08);position:relative;z-index:2}
.header .wrap{display:flex;justify-content:space-between;align-items:center;height:72px}
.brand{display:flex;align-items:center;gap:10px;font-family:"Raleway",sans-serif;font-weight:700;font-size:20px;color:var(--navy)}
.brand i{width:26px;height:26px;background:var(--navy);display:block}
.nav{display:flex;gap:26px;font-size:13px;font-weight:600;color:var(--ink)}
.nav .on{color:var(--cyan)}

.hero{height:500px;position:relative;text-align:center;color:var(--white);
  background:radial-gradient(ellipse at 50% 40%,#2d4a70 0%,#182a44 55%,#0e1a2c 100%)}
.hero h1{padding-top:160px;font-size:62px;font-weight:800;letter-spacing:1px}
.hero p{font-size:15px;margin-top:18px;line-height:1.5}
.btn{display:inline-block;background:var(--cyan);color:var(--white);font-size:11px;font-weight:700;
  letter-spacing:1px;text-transform:uppercase;padding:12px 26px}
.hero .btn{margin-top:36px}

.about{height:420px;display:flex}
.about .art{width:460px;height:300px;margin:60px 0 0 80px;
  background:linear-gradient(180deg,#ffffff 0%,#eaf5fb 100%)}
.about .copy{width:560px;margin:64px 0 0 40px}
.about h3{font-size:15px;color:var(--cyan);font-weight:700;line-height:1.4;margin-bottom:14px}
.about p{font-size:11px;color:var(--muted);margin-bottom:12px}

.services{height:410px;background:var(--soft);text-align:center}
.services h2{font-size:14px;color:var(--cyan);padding-top:30px;font-weight:700}
.services h2:after{content:"";display:block;width:40px;height:2px;background:var(--cyan);margin:6px auto 0}
.svc-row{display:flex;justify-content:center;gap:40px;margin-top:40px}
.svc{width:210px}
.svc .ring{width:130px;height:130px;border-radius:50%;border:2px solid var(--line);background:var(--white);margin:0 auto;display:flex;align-items:center;justify-content:center}
.svc .dot{width:58px;height:58px;border-radius:50%;background:#6b7078;display:flex;align-items:center;justify-content:center}
.svc.on .ring{border-color:var(--green)}
.svc.on .dot{background:var(--green)}
.svc h4{font-size:16px;font-weight:500;margin-top:22px}
.svc.on h4{color:var(--green)}
.svc p{font-size:10px;color:var(--muted);margin-top:6px;line-height:1.5}
.services .btn{margin-top:30px}

.devices{height:460px;display:flex}
.devices .art{width:520px;height:290px;margin:60px 0 0 60px;
  background:linear-gradient(135deg,#e9eef3 0%,#d5dde6 100%)}
.feats{margin:70px 0 0 40px;width:460px}
.feat{display:flex;gap:18px;margin-bottom:28px}
.feat .ic{width:40px;height:40px;border-radius:50%;background:#e8ebef;flex:none;display:flex;align-items:center;justify-content:center}
.feat h4{font-size:17px;font-weight:500;margin-bottom:4px}
.feat p{font-size:10px;color:var(--muted);line-height:1.5}
.feats .btn{margin:6px 0 0 70px}

.solutions{height:280px;background:var(--soft);text-align:center}
.solutions h2{font-size:30px;font-weight:600;padding-top:68px}
.solutions p{font-size:12px;color:var(--muted);margin-top:10px}
.solutions .btns{margin-top:34px;display:flex;justify-content:center;gap:24px}
.btn.ghost{background:var(--white);color:var(--cyan);border:1px solid var(--cyan)}

.footer{height:370px;background:var(--dark);color:#a6abb3;font-size:10px}
.footer .wrap{display:flex;gap:40px;padding-top:40px}
.fcol{width:230px}
.fcol h4{color:var(--white);font-size:13px;font-weight:700;margin-bottom:16px}
.flogo{font-family:"Raleway",sans-serif;font-size:22px;font-weight:700;color:var(--white);margin-bottom:14px}
.fcol li{list-style:none;margin-bottom:10px;line-height:1.4}
.socials{display:flex;gap:6px;margin-top:14px}
.socials span{width:18px;height:18px;border:1px solid #555b64}
.field{height:26px;background:#2c3037;margin-top:10px;display:flex;justify-content:flex-end}
.field b{width:30px;background:var(--cyan)}
.copyright{height:48px;background:var(--darker);color:#8b9099;font-size:10px;text-align:center;line-height:48px}
</style>
</head>
<body>
<div class="topbar"><div class="wrap">
  <div><span>+61 (02) 5550 1842</span><span>Port Aldine NSW</span></div>
  <div>hello@halvex.com.au</div>
</div></div>

<header class="header"><div class="wrap">
  <div class="brand"><i></i>Halvex Technologies</div>
  <nav class="nav"><span class="on">Home</span><span>Services</span><span>Networks</span><span>Managed IT</span><span>Web</span><span>Apps</span><span>Internet</span><span>Contact</span></nav>
</div></header>

<section class="hero" role="img" aria-label="Dark blue network backdrop with connected points of light">
  <h1>THROUGH HALVEX TECHNOLOGIES</h1>
  <p>Through Halvex Technologies, companies outsource all the expertise<br>they need to secure their systems and optimise the output of their people and IT resources</p>
  <a class="btn">Check It Out</a>
</section>

<section class="about">
  <div class="art" role="img" aria-label="Line illustration of a rocket launching from a computer screen"></div>
  <div class="copy">
    <h3>What would it take for your information systems to actually improve the performance of your organisation?</h3>
    <p>Through Halvex Technologies, companies outsource all the expertise they need to secure their systems and optimise the output of their people and IT resources, without the expense of maintaining large internal IT departments.</p>
    <p>With a decade of experience, Halvex Technologies understands the challenges faced by SMEs: the need to manage and build networks, support complex business systems and keep every device secure, stable and available.</p>
    <p>Our team will look after your systems end to end: they plan and build reliable networks, manage cloud and email services, and provide helpdesk support so that your staff stay productive and your data stays safe every day.</p>
    <p>For the ultimate peace of mind, Halvex Technologies keeps your systems running at their best.</p>
  </div>
</section>

<section class="services">
  <h2>Web</h2>
  <div class="svc-row">
    <div class="svc"><div class="ring"><div class="dot"><svg width="24" height="24" viewBox="0 0 24 24"><path d="M5 19l10-10 2 2-10 10H5z" fill="#fff"/></svg></div></div><h4>Content Management</h4><p>Lorem ipsum dolor sit amet, consectetuer adipiscing elit, sed diam nonummy nibh euismod tincidunt ut.</p></div>
    <div class="svc"><div class="ring"><div class="dot"><svg width="24" height="24" viewBox="0 0 24 24"><rect x="4" y="6" width="16" height="11" fill="none" stroke="#fff" stroke-width="2"/></svg></div></div><h4>Website Design</h4><p>Lorem ipsum dolor sit amet, consectetuer adipiscing elit, sed diam nonummy nibh euismod tincidunt ut.</p></div>
    <div class="svc on"><div class="ring"><div class="dot"><svg width="24" height="24" viewBox="0 0 24 24"><circle cx="12" cy="12" r="5" fill="none" stroke="#fff" stroke-width="2"/><path d="M12 3v4M12 17v4M3 12h4M17 12h4" stroke="#fff" stroke-width="2"/></svg></div></div><h4>Digital Strategy</h4><p>Lorem ipsum dolor sit amet, consectetuer adipiscing elit, sed diam nonummy nibh euismod tincidunt ut.</p></div>
    <div class="svc"><div class="ring"><div class="dot"><svg width="24" height="24" viewBox="0 0 24 24"><circle cx="7" cy="12" r="2.5" fill="#fff"/><circle cx="17" cy="7" r="2.5" fill="#fff"/><circle cx="17" cy="17" r="2.5" fill="#fff"/><path d="M7 12L17 7M7 12l10 5" stroke="#fff" stroke-width="1.5"/></svg></div></div><h4>Social Media Management</h4><p>Lorem ipsum dolor sit amet, consectetuer adipiscing elit, sed diam nonummy nibh euismod tincidunt ut.</p></div>
  </div>
  <a class="btn">View More</a>
</section>

<section class="devices">
  <div class="art" role="img" aria-label="Tablet, phone and laptop showing a dashboard"></div>
  <div class="feats">
    <div class="feat"><div class="ic"><svg width="18" height="18" viewBox="0 0 24 24"><circle cx="11" cy="11" r="6" fill="none" stroke="#6b7078" stroke-width="2"/><path d="M16 16l5 5" stroke="#6b7078" stroke-width="2"/></svg></div><div><h4>Discovery &amp; Strategy</h4><p>Lorem ipsum dolor sit amet, consectetuer adipiscing elit, sed diam nonummy nibh euismod tincidunt ut laoreet dolore magna.</p></div></div>
    <div class="feat"><div class="ic"><svg width="18" height="18" viewBox="0 0 24 24"><circle cx="12" cy="8" r="4" fill="#6b7078"/><path d="M4 21c1-5 15-5 16 0" fill="#6b7078"/></svg></div><div><h4>User Experience Design</h4><p>Lorem ipsum dolor sit amet, consectetuer adipiscing elit, sed diam nonummy nibh euismod tincidunt ut laoreet dolore magna.</p></div></div>
    <div class="feat"><div class="ic"><svg width="18" height="18" viewBox="0 0 24 24"><rect x="7" y="3" width="10" height="18" rx="2" fill="none" stroke="#6b7078" stroke-width="2"/></svg></div><div><h4>Mobile App Development</h4><p>Lorem ipsum dolor sit amet, consectetuer adipiscing elit, sed diam nonummy nibh euismod tincidunt ut laoreet dolore magna.</p></div></div>
    <a class="btn">View More</a>
  </div>
</section>

<section class="solutions">
  <h2>Internet Solutions</h2>
  <p>Halvex Technologies is a 'Native, Tailored and Fast' partner. We have access to a different 'tier' of support so we get things fixed for you<br>faster when there is a problem.</p>
  <div class="btns"><a class="btn">Read More</a><a class="btn ghost">Start Fibre With Halvex Today</a></div>
</section>

<footer class="footer"><div class="wrap">
  <div class="fcol">
    <div class="flogo">bravlo</div>
    <p>Lorem ipsum dolor sit amet, consectetuer adipiscing elit, sed diam nonummy nibh euismod tincidunt ut laoreet dolore magna aliquam erat volutpat.</p>
    <p style="margin-top:10px">Port Aldine NSW<br>+61 (02) 5550 1842</p>
    <div class="socials"><span></span><span></span><span></span><span></span><span></span></div>
  </div>
  <div class="fcol"><h4>Latest Posts</h4><ul>
    <li>How to plan a secure network for a small office</li>
    <li>Five signs your business needs managed IT</li>
    <li>Moving your email to the cloud step by step</li>
    <li>Choosing the right backup plan this year</li>
    <li>Why fast internet matters for your team</li>
  </ul></div>
  <div class="fcol"><h4>Latest Tweets</h4><ul>
    <li>New guide on keeping office devices patched and safe is now live on our blog. 2 days ago</li>
    <li>Our helpdesk hours are extended over the holiday period for all clients. 5 days ago</li>
    <li>Thanks to everyone who came along to our cloud workshop last week. 1 week ago</li>
  </ul></div>
  <div class="fcol"><h4>Latest Posts</h4><ul>
    <li>Simple steps to stronger passwords</li>
    <li>Getting the most from your new website</li>
  </ul>
    <h4 style="margin-top:18px">Newsletter</h4>
    <p>Sign up for news and tips.</p>
    <div class="field"><b></b></div>
  </div>
</div></footer>
<div class="copyright">Copyright © Halvex Technologies</div>
</body>
</html>
```